political advertisement for magazine

9.135 in 12.125 in. My wife is running for Judge. She needs an ad for an African-American Magazine ASAP . The ad is about a testimonial by one of her clients that makes her relatable to the African-American community. I am uploading the text for the testimonial, the picture of my wife and her client, her logo, a possible backdrop and also a slogan.

This is going in a church publication geared toward the African American Community

• The image of all the people in the back. On top of that image, you have "The people stand behind Lorena for Circuit Court Judge". Also you have a letter from her client with a picture of both of them. Also include the vote for Lorena logo and her headshot. The above is just my idea if you have an idea that is totally different but portrays that Lorena is for the people, I am ok with that too. thanks!

```html
<!DOCTYPE html>
<html lang="en">
<head>
<meta charset="utf-8">
<title>Lorena for Circuit Court Judge – Magazine Ad</title>
<link href="https://fonts.googleapis.com/css2?family=Open+Sans:ital,wght@0,400;0,600;0,700;0,800;1,400&display=swap" rel="stylesheet">
<style>
  :root {
    --royal: #2557b3;
    --royal-deep: #2350a6;
    --red: #ee1111;
    --white: #ffffff;
    --mist: #e4e4e4;
    --stage: #ece9e4;
  }
  * { box-sizing: border-box; margin: 0; padding: 0; }
  html, body {
    width: 719px; height: 1200px; overflow: hidden;
    background: var(--stage);
    font-family: "Open Sans", Arial, sans-serif;
  }
  .ad {
    position: absolute; left: 0; top: 123px;
    width: 719px; height: 954px; overflow: hidden;
    background: var(--mist);
  }
  .crowd-blue {
    position: absolute; left: 0; top: 0; width: 719px; height: 260px;
    background: linear-gradient(180deg, #2557b3 0%, #2a5cb6 55%, #2350a6 100%);
  }
  .crowd-grey {
    position: absolute; left: 0; top: 260px; width: 719px; height: 381px;
    background: linear-gradient(180deg, #d3d3d3 0%, #ececec 40%, #e2e2e2 100%);
  }
  .wave { position: absolute; left: 0; top: 236px; width: 719px; height: 120px; }
  .headline { position: absolute; left: 0; top: 0; width: 719px; height: 230px; color: var(--white); }
  .headline span {
    position: absolute; left: 0; width: 719px; text-align: center; line-height: 1; white-space: nowrap;
  }
  .headline .lead, .headline .office { font-weight: 700; font-size: 31px; letter-spacing: 0.3px; }
  .headline .lead { top: 58px; }
  .headline .office { top: 189px; }
  .headline .name {
    top: 76px; font-weight: 800; font-size: 112px; letter-spacing: -2px;
    background: linear-gradient(180deg, #ff3b3b 0%, #e80c0c 60%, #b80406 100%);
    -webkit-background-clip: text; background-clip: text; color: transparent;
    -webkit-text-stroke: 2px var(--white);
  }
  .headshot {
    position: absolute; left: 0; top: 306px; width: 317px; height: 335px;
    background: radial-gradient(ellipse at 50% 30%, #d7b39c 0%, #a0755a 30%, #4a3428 60%, #151515 100%);
  }
  .campaign-name {
    position: absolute; left: 330px; top: 430px; width: 370px;
    text-align: center; color: var(--red); font-weight: 700; font-size: 40px; line-height: 48px;
  }
  .testimonial {
    position: absolute; left: 0; top: 641px; width: 719px; height: 243px;
    background: var(--red);
  }
  .client-photo-ring {
    position: absolute; left: 19px; top: 15px; width: 216px; height: 216px;
    border-radius: 50%; border: 2px solid var(--white);
  }
  .client-photo {
    position: absolute; left: 12px; top: 12px; width: 188px; height: 188px; border-radius: 50%;
    background: radial-gradient(circle at 50% 40%, #d9c2b0 0%, #8a6a57 35%, #3f6b3a 70%, #2b4a2a 100%);
  }
  .quote-mark { position: absolute; color: var(--white); font-weight: 800; font-size: 54px; line-height: 1; }
  .quote-mark.open { left: 238px; top: 20px; }
  .quote-mark.close { left: 492px; top: 178px; }
  .quote-body {
    position: absolute; left: 280px; top: 32px; width: 410px;
    color: var(--white); font-size: 11.3px; line-height: 15.6px; text-align: justify;
  }
  .quote-body p + p { margin-top: 9px; }
  .signoff {
    position: absolute; right: 30px; top: 190px; text-align: right;
    color: var(--white); font-size: 15px; line-height: 21px;
  }
  .signoff strong { font-weight: 700; }
  .disclaimer {
    position: absolute; left: 0; top: 884px; width: 719px; height: 70px;
    background: linear-gradient(180deg, #2563b0 0%, #1c4a92 100%);
    color: var(--white); font-style: italic; font-size: 12.3px; line-height: 18px;
    text-align: center; padding-top: 16px;
  }
</style>
</head>
<body>
  <main class="ad">
    <div class="crowd-blue" role="img" aria-label="Collage of smiling community faces tinted royal blue"></div>
    <div class="crowd-grey" role="img" aria-label="Collage of smiling community faces in light greyscale"></div>

    <svg class="wave" viewBox="0 0 719 120" aria-hidden="true">
      <path d="M0 0 H719 V48 C650 66 590 64 520 52 C380 26 200 18 0 38 Z" fill="#2350a6"/>
      <path d="M0 40 C200 22 380 30 520 56 C600 70 670 66 719 50" fill="none" stroke="#ffffff" stroke-width="3"/>
      <path d="M0 44 C200 26 380 34 520 60 C600 74 670 70 719 54 L719 60 C640 100 560 112 470 106 C300 96 150 58 0 54 Z" fill="#ee1111"/>
    </svg>

    <h1 class="headline">
      <span class="lead">THE PEOPLE STAND BEHIND</span>
      <span class="name">LORENA</span>
      <span class="office">FOR CIRCUIT COURT JUDGE</span>
    </h1>

    <div class="headshot" role="img" aria-label="Headshot of Lorena smiling, wearing a black blazer and pearl necklace"></div>

    <p class="campaign-name">Lorena<br>Ellison Carter</p>

    <section class="testimonial">
      <div class="client-photo-ring">
        <div class="client-photo" role="img" aria-label="Lorena shaking hands with her client in a garden"></div>
      </div>
      <span class="quote-mark open">“</span>
      <div class="quote-body">
        <p>For the past few years, Lorena Ellison Carter has been my lawyer. She has always strived to provide excellence in legal services. Her almost encyclopedic knowledge of the law makes for a flawless, precise, navigation of the legal system, with results.</p>
        <p>She is the epitome of professionalism, that is aptly balanced by her calm persona. Her empathy is more than commendable, and her legal experience unmatched.</p>
        <p>Lorena Ellison Carter is truly one of kind, deserving of all accolades, appointments, and accomplishments.</p>
      </div>
      <span class="quote-mark close">”</span>
      <div class="signoff">Yours Truly,<br><strong>Raymond Whitaker</strong></div>
    </section>

    <footer class="disclaimer">
      Political Advertisement paid for and approved by the Committee to Elect Lorena<br>
      Ellison Carter, no party affiliation, for Circuit Court Judge
    </footer>
  </main>
</body>
</html>
```